Velkano Holdings Ltd - An invesmtent & trading company needs a web design

We need a web design for our company based in Cyprus. The company was founded in 2009. We have continuously grown and now invest & trade all over the world.

Velkano Holdings ltd. specializes in the buying and selling of crude oil, precious metals and the investment in properties.

We know that trust is of the utmost importance when it comes to business and the design should communicate this to prospective business partners. Find attached the company logo. The colour scheme for the website should use similar colours and ideally incorporate the logo in some shape or form as well.

Target Market(s)

Oil Traders, Metall Traders, Property Investments

Industry/Entity Type

Trade

Coding

Coded - Design and coding required

Number of Pages Required

4 page

Font styles to use
Sans Serif

Requirements
Must have
• Mainpage,
• About Us
• Partners
• Legal Notice

```html
<!DOCTYPE html>
<html lang="en">
<head>
<meta charset="utf-8">
<title>Velkano Holdings Ltd</title>
<link rel="stylesheet" href="https://fonts.googleapis.com/css2?family=Roboto:wght@400;700&family=Roboto+Condensed:wght@400;700&display=swap">
<style>
:root{
  --blue:#0a66c2;
  --blue-dark:#06489a;
  --blue-deep:#0b3f86;
  --nav:#1583d8;
  --ink:#333;
  --muted:#666;
  --footer:#2c2f33;
  --white:#fff;
}
*{box-sizing:border-box;margin:0;padding:0}
html,body{width:831px;height:1200px;overflow:hidden}
body{font-family:"Roboto",Arial,sans-serif;color:var(--ink);background:var(--white);position:relative}
.site-header{position:absolute;top:0;left:0;width:831px;height:78px;background:var(--white)}
.brand{position:absolute;left:92px;top:14px;display:flex;align-items:center;gap:10px}
.brand-square{width:44px;height:44px;background:var(--blue)}
.brand-name{font-family:"Roboto Condensed",sans-serif;font-weight:700;font-size:25px;color:var(--blue-dark);line-height:1;letter-spacing:.5px}
.callout{position:absolute;right:92px;top:6px;display:flex;align-items:center;gap:8px}
.callout .phone-box{width:28px;height:28px;background:var(--blue);display:flex;align-items:center;justify-content:center}
.callout small{display:block;font-size:10px;color:var(--muted)}
.callout strong{display:block;font-family:"Roboto Condensed",sans-serif;font-size:17px;color:var(--blue-dark)}
.main-nav{position:absolute;right:92px;top:48px;height:30px;display:flex;background:var(--blue)}
.main-nav a{color:var(--white);text-decoration:none;font-size:12px;padding:0 12px;line-height:30px}
.main-nav a.active{background:var(--nav)}
.hero{position:absolute;top:78px;left:0;width:831px;height:310px;background:linear-gradient(135deg,#c9d3dc 0%,#8a9aa8 40%,#dfe4e8 70%,#5f6f7d 100%)}
.hero-arrow{position:absolute;top:140px;width:22px;height:28px;background:rgba(0,0,0,.6);display:flex;align-items:center;justify-content:center}
.hero-arrow.prev{left:0}.hero-arrow.next{right:0}
.hero-caption{position:absolute;left:90px;right:90px;bottom:8px;height:28px;background:rgba(10,40,80,.65);color:var(--white);font-family:"Roboto Condensed",sans-serif;font-size:15px;line-height:28px;text-align:center}
.about{position:absolute;top:388px;left:0;width:831px;height:167px;text-align:center;padding-top:24px}
.about h2{font-family:"Roboto Condensed",sans-serif;font-size:20px;color:var(--blue);font-weight:700}
.about h2 span{color:var(--blue-dark)}
.rule{width:90px;height:2px;background:var(--blue);margin:6px auto 10px}
.about p{width:620px;margin:0 auto;font-size:8.5px;line-height:13px;color:var(--muted)}
.about .more{display:inline-block;margin-top:12px;font-size:10px;font-weight:700;color:var(--blue-dark);border-bottom:1px solid var(--blue-dark)}
.services{position:absolute;top:555px;left:0;width:831px;height:360px;background:radial-gradient(ellipse at 50% 45%,#1c7fe0 0%,var(--blue) 45%,var(--blue-deep) 100%);color:var(--white);text-align:center;padding-top:22px}
.services h2{font-family:"Roboto Condensed",sans-serif;font-size:19px;font-weight:700}
.services .rule{background:var(--white)}
.services .lead{width:600px;margin:0 auto;font-size:8.5px;line-height:13px;opacity:.9}
.mark-faint{position:absolute;left:50%;transform:translateX(-50%);display:flex;align-items:center;gap:8px;opacity:.22}
.mark-faint .sq{background:var(--white)}
.mark-faint .nm{font-family:"Roboto Condensed",sans-serif;font-weight:700;color:var(--white)}
.service{position:absolute;width:170px;text-align:center}
.service .icon{width:64px;height:64px;border-radius:50%;background:var(--white);margin:0 auto 8px;display:flex;align-items:center;justify-content:center}
.service h3{font-size:12px;font-weight:400;margin-bottom:4px}
.service p{font-size:8.5px;line-height:12px;opacity:.9}
.site-footer{position:absolute;top:915px;left:0;width:831px;height:257px;background:var(--footer);color:#ddd}
.map{position:absolute;inset:0;background:linear-gradient(160deg,#3a3e43 0%,#2a2d31 50%,#34383d 100%)}
.contact{position:absolute;left:92px;top:20px;width:250px}
.contact h4{font-size:12px;font-weight:400;color:var(--white);border-bottom:1px solid #666;padding-bottom:6px;margin-bottom:10px}
.contact-row{display:flex;gap:8px;margin-bottom:10px;font-size:8.5px;line-height:12px}
.contact-row .ico{width:12px;flex:none}
.contact-row b{display:block;font-weight:400;color:var(--white)}
.footer-mark{top:92px}
.inquiry{position:absolute;right:92px;top:20px;width:200px;background:rgba(255,255,255,.1);padding:0 0 12px}
.inquiry-head{background:#eee;color:#333;height:34px;display:flex;align-items:center;gap:8px;padding:0 10px;font-size:12px;font-weight:700}
.inquiry small{display:block;font-size:7.5px;color:#ccc;padding:6px 10px}
.field{height:20px;margin:0 10px 7px;background:#fff;font-size:7.5px;color:#999;padding:5px 6px}
.field.area{height:38px}
.submit{margin:2px 10px 0;width:56px;height:20px;background:var(--blue);color:#fff;font-size:8px;display:flex;align-items:center;justify-content:center}
.copyright{position:absolute;top:1172px;left:0;width:831px;height:28px;background:var(--blue);color:var(--white);font-size:8.5px;line-height:28px;text-align:center}
</style>
</head>
<body>
<header class="site-header">
  <div class="brand"><div class="brand-square"></div><div class="brand-name">VELKANO<br>HOLDINGS LTD.</div></div>
  <div class="callout">
    <div class="phone-box"><svg width="14" height="14" viewBox="0 0 24 24"><path fill="#fff" d="M6.6 10.8a15 15 0 0 0 6.6 6.6l2.2-2.2c.3-.3.7-.4 1-.2 1.1.4 2.3.6 3.6.6.6 0 1 .4 1 1V20c0 .6-.4 1-1 1A17 17 0 0 1 3 4c0-.6.4-1 1-1h3.5c.6 0 1 .4 1 1 0 1.3.2 2.5.6 3.6.1.3 0 .7-.2 1z"/></svg></div>
    <div><small>Call for Today</small><strong>123-456-7890</strong></div>
  </div>
  <nav class="main-nav"><a class="active">Home</a><a>About</a><a>Partners</a><a>Legal Notice</a><a>Contact</a></nav>
</header>

<section class="hero" role="img" aria-label="Photo of business people reviewing financial charts and documents">
  <div class="hero-arrow prev"><svg width="8" height="12"><path d="M7 1 2 6l5 5" stroke="#fff" stroke-width="2" fill="none"/></svg></div>
  <div class="hero-arrow next"><svg width="8" height="12"><path d="m1 1 5 5-5 5" stroke="#fff" stroke-width="2" fill="none"/></svg></div>
  <div class="hero-caption">We specialize in the buying and selling of crude oil, precious metals &amp; the investment in properties.</div>
</section>

<section class="about">
  <h2>About <span>Velkano Holdings Ltd.</span></h2>
  <div class="rule"></div>
  <p>Lorem ipsum dolor sit amet, consectetuer adipiscing elit, sed diam nonummy nibh euismod tincidunt ut laoreet dolore magna aliquam erat volutpat. Ut wisi enim ad minim veniam, quis nostrud exerci tation ullamcorper suscipit lobortis nisl ut aliquip ex ea commodo consequat. Duis autem vel eum iriure dolor in hendrerit in vulputate velit esse molestie consequat, vel illum dolore eu feugiat nulla facilisis at vero eros et accumsan et iusto odio dignissim qui blandit praesent luptatum zzril delenit augue duis dolore te feugait nulla facilisi. Nam liber tempor cum soluta nobis eleifend option congue nihil imperdiet doming id quod mazim placerat facer possim assum.</p>
  <span class="more">Read More</span>
</section>

<section class="services">
  <h2>We Specialize In The Buying And Selling Of</h2>
  <div class="rule"></div>
  <p class="lead">Lorem ipsum dolor sit amet, consectetuer adipiscing elit, sed diam nonummy nibh euismod tincidunt ut laoreet dolore magna aliquam erat volutpat. Ut wisi enim ad minim veniam, quis nostrud exerci tation ullamcorper suscipit lobortis nisl ut aliquip.</p>
  <div class="mark-faint" style="top:96px"><div class="sq" style="width:30px;height:30px"></div><div class="nm" style="font-size:26px">VELKANO</div></div>
  <div class="service" style="left:110px;top:138px">
    <div class="icon"><svg width="26" height="30" viewBox="0 0 26 30"><path d="M13 1C9 9 3 14 3 20a10 10 0 0 0 20 0c0-6-6-11-10-19z" fill="var(--blue)"/></svg></div>
    <h3>Crude Oil</h3>
    <p>Lorem ipsum dolor sit amet, consectetuer adipiscing elit, sed diam nonummy nibh euismod tincidunt ut.</p>
  </div>
  <div class="service" style="left:540px;top:138px">
    <div class="icon"><svg width="30" height="30" viewBox="0 0 30 30"><path d="M4 28V10l11-7 11 7v18z" fill="var(--blue)"/><rect x="12" y="18" width="6" height="10" fill="#fff"/></svg></div>
    <h3>Investments in Properties</h3>
    <p>Lorem ipsum dolor sit amet, consectetuer adipiscing elit, sed diam nonummy nibh euismod tincidunt ut.</p>
  </div>
  <div class="service" style="left:330px;top:208px">
    <div class="icon"><svg width="32" height="24" viewBox="0 0 32 24"><path d="M5 13h10l2 9H3zM17 13h10l2 9H15zM11 2h10l2 9H9z" fill="var(--blue)"/></svg></div>
    <h3>Precious Metals</h3>
    <p>Lorem ipsum dolor sit amet, consectetuer adipiscing elit, sed diam nonummy nibh euismod tincidunt ut.</p>
  </div>
</section>

<footer class="site-footer">
  <div class="map" role="img" aria-label="Street map showing the office location"></div>
  <div class="mark-faint footer-mark"><div class="sq" style="width:40px;height:40px"></div><div class="nm" style="font-size:34px">VELKANO</div></div>
  <div class="contact">
    <h4>Contact Information</h4>
    <div class="contact-row"><svg class="ico" viewBox="0 0 12 16" height="14"><path d="M6 0a5 5 0 0 0-5 5c0 4 5 11 5 11s5-7 5-11a5 5 0 0 0-5-5z" fill="#ddd"/><circle cx="6" cy="5" r="2" fill="#2c2f33"/></svg><div><b>Main Office</b>Street Name, City Name<br>State Country</div></div>
    <div class="contact-row"><svg class="ico" viewBox="0 0 24 24" height="12"><path fill="#ddd" d="M6.6 10.8a15 15 0 0 0 6.6 6.6l2.2-2.2c.3-.3.7-.4 1-.2 1.1.4 2.3.6 3.6.6.6 0 1 .4 1 1V20c0 .6-.4 1-1 1A17 17 0 0 1 3 4c0-.6.4-1 1-1h3.5c.6 0 1 .4 1 1 0 1.3.2 2.5.6 3.6.1.3 0 .7-.2 1z"/></svg><div><b>Telephone</b>123-456-7890</div></div>
    <div class="contact-row"><svg class="ico" viewBox="0 0 16 12" height="10"><rect width="16" height="12" fill="#ddd"/><path d="m0 0 8 7 8-7" stroke="#2c2f33" fill="none"/></svg><div><b>Email</b>info@velkanoholdings.com</div></div>
    <div class="contact-row"><svg class="ico" viewBox="0 0 12 12" height="12"><rect width="12" height="12" fill="#ddd"/></svg><div><b>Social</b>social.example/velkanoholdings</div></div>
  </div>
  <div class="inquiry">
    <div class="inquiry-head"><svg width="16" height="14" viewBox="0 0 16 14"><path d="M1 1h14v9H6l-4 3v-3H1z" fill="#555"/></svg>QUICK INQUIRY</div>
    <small>We will get back to you shortly after your inquiry.</small>
    <div class="field">Name</div>
    <div class="field">Email</div>
    <div class="field">Phone</div>
    <div class="field area">Message</div>
    <div class="submit">SUBMIT</div>
  </div>
</footer>
<div class="copyright">© 2014 Velkano Holdings Ltd. All Rights Reserved.</div>
</body>
</html>
```